Plakat-Design für Herbstausstellung
Zielgruppe
Wir sind im Motorradhandel, inkl. Motorrad Bekleidung/Zubehör, tätig. Für unsere Herbstausstellung brauchen wir ein neues Plakat-Design. Unsere Zielgruppe sind im allgemeinen Männer und Frauen im Alter von 18-65 Jahre.
Aufgabenstellung
Das Plakat sollte Hochformat sein.
Angaben welche ersichtlich sein sollten: Unser Logo (Rad Kessel);Herbst-Ausstellung; Datum der Herbstausstellung (20.-22.10.17); Öffnungszeiten (Fr. 14-19h/Sa. 8-19h/So. 9-16h); Saisonausverkauf mit -20% auf Motorradbekleidung und Zubehör (nur auf nicht reduzierte Lagerware); Unsere Livemusik im Festzelt ( Freitag ab 20.00 Uhr Twistabend Nacht mit Kurvenfeger, Samstag ab 20.00 Uhr Festmusik mit Bergklang-Alpin, Sonntag Matinée 09.00-16.00 Uhr), www.rad-kessel.ch)<- kann klein dargestellt werden; Unsere Markenvertretungen (VRX, GLP, Hanoka)
Vom Design her ist der Kreativität keine Grenze gesetzt (In den Dateianhängen ist unser altes Plakat-Design beigefügt, als Anhaltspunkt für den Inhalt). Es sollte modern und einladend wirken. Wir verwenden im Normalfall den Font "Impact", dies stellt aber kein Killerkriterium dar.

```html
<!DOCTYPE html>
<html lang="de">
<head>
<meta charset="utf-8">
<title>Herbstausstellung – Rad Kessel</title>
<link rel="stylesheet" href="https://fonts.googleapis.com/css2?family=Anton&family=Oswald:wght@500;600;700&family=Archivo:ital,wght@0,800;1,800&display=swap">
<style>
  :root {
    --stage: #2b2b2b;
    --red: #c8101e;
    --red-deep: #7a0610;
    --red-bright: #d81a26;
    --orange: #f3a31c;
    --white: #ffffff;
    --ink: #2a2220;
    --sand-light: #f3ead6;
    --sand: #c9ad7d;
    --umber: #6b5138;
  }
  html, body {
    margin: 0;
    padding: 0;
    width: 716px;
    height: 1200px;
    overflow: hidden;
    background: var(--stage);
  }
  .poster {
    position: absolute;
    left: 18px;
    top: 116px;
    width: 680px;
    height: 968px;
    overflow: hidden;
    background: var(--red-deep);
    font-family: "Oswald", "Anton", sans-serif;
    color: var(--white);
  }
  .hero-photo {
    position: absolute;
    left: 0; top: 0;
    width: 680px; height: 557px;
    background:
      radial-gradient(ellipse 55% 40% at 80% 20%, var(--sand-light) 0%, rgba(243,234,214,0) 70%),
      radial-gradient(ellipse 40% 45% at 55% 55%, #8a6a4a 0%, rgba(138,106,74,0) 75%),
      linear-gradient(180deg, #d8c6a2 0%, var(--sand) 45%, var(--umber) 100%);
  }
  .brand-bar {
    position: absolute;
    left: 196px; top: 0;
    width: 276px; height: 49px;
    background: var(--red);
    display: flex; align-items: center; justify-content: center;
    font-family: "Anton", sans-serif;
    font-size: 31px;
    letter-spacing: 1px;
    color: var(--white);
  }
  .brand-tagline {
    position: absolute;
    left: 196px; top: 54px; width: 276px;
    text-align: center;
    font-family: "Archivo", sans-serif;
    font-style: italic;
    font-weight: 800;
    font-size: 12.5px;
    color: var(--ink);
  }
  .headline {
    position: absolute;
    left: 0; top: 0;
    width: 680px; height: 560px;
  }
  .info-panel {
    position: absolute;
    left: 0; top: 557px;
    width: 680px; height: 411px;
    background:
      radial-gradient(ellipse 60% 50% at 85% 90%, rgba(150,20,20,0.6) 0%, rgba(150,20,20,0) 70%),
      linear-gradient(180deg, var(--red-bright) 0%, #b00c18 35%, var(--red-deep) 100%);
  }
  .event-date {
    position: absolute;
    left: 0; top: 557px;
    width: 680px; height: 100px;
  }
  .details {
    position: absolute;
    left: 38px; top: 652px;
    width: 600px;
    font-weight: 600;
    font-size: 19px;
    line-height: 23px;
  }
  .details p { margin: 0; }
  .details .gap { margin-top: 6px; }
  .details .label { letter-spacing: 2px; font-weight: 700; }
  .accent { color: var(--orange); letter-spacing: 1px; font-weight: 700; }
  .contact {
    position: absolute;
    left: 38px; top: 872px;
    font-style: normal;
    font-weight: 600;
    font-size: 17px;
    line-height: 20px;
  }
  .partners {
    position: absolute;
    left: 498px; top: 848px;
    width: 160px; height: 80px;
    font-family: "Anton", sans-serif;
    color: var(--white);
  }
  .partner { position: absolute; font-size: 22px; line-height: 1; }
  .partner-vrx { left: 0; top: 6px; display: flex; align-items: center; gap: 5px; }
  .partner-vrx .dot {
    width: 18px; height: 18px; border-radius: 50%;
    border: 2px solid var(--white); box-sizing: border-box;
  }
  .partner-glp { left: 92px; top: 6px; }
  .partner-hanoka { left: 76px; top: 50px; }
  .web-address {
    position: absolute;
    left: 227px; top: 943px;
    width: 226px; height: 25px;
    background: var(--red);
    display: flex; align-items: center; justify-content: center;
    font-weight: 600;
    font-size: 14px;
    letter-spacing: 3px;
  }
</style>
</head>
<body>
  <main class="poster">
    <div class="hero-photo" role="img" aria-label="Foto: Motorradfahrer mit Helm auf einer Reiseenduro von hinten, im warmen Gegenlicht der Herbstsonne"></div>

    <div class="brand-bar">RAD KESSEL</div>
    <div class="brand-tagline">DAS TÖFFHAUS im Mittelland</div>

    <div class="info-panel"></div>

    <svg class="headline" viewBox="0 0 680 560" aria-label="Herbst-Ausstellung">
      <defs>
        <linearGradient id="herbstFill" x1="0" y1="0" x2="0" y2="1">
          <stop offset="0" stop-color="#ffffff" stop-opacity="0.92"/>
          <stop offset="1" stop-color="#f2eee8" stop-opacity="0.85"/>
        </linearGradient>
        <linearGradient id="ausstellungFill" x1="0" y1="0" x2="0" y2="1">
          <stop offset="0" stop-color="#e6e2dc"/>
          <stop offset="1" stop-color="#9a948e"/>
        </linearGradient>
      </defs>
      <text x="0" y="459" font-family="Anton, sans-serif" font-size="236" fill="url(#herbstFill)" textLength="680" lengthAdjust="spacingAndGlyphs">HERBST</text>
      <text x="-4" y="551" font-family="Anton, sans-serif" font-size="124" fill="url(#ausstellungFill)" textLength="688" lengthAdjust="spacingAndGlyphs">AUSSTELLUNG</text>
    </svg>

    <svg class="event-date" viewBox="0 0 680 100" aria-label="20.-22. Oktober 2017">
      <text x="43" y="80" font-family="Anton, sans-serif" font-size="58" fill="#ffffff" textLength="594" lengthAdjust="spacing">20.-22. OKTOBER 2017</text>
    </svg>

    <section class="details">
      <p><span class="label">ÖFFNUNGSZEITEN</span>&nbsp; Fr. 14 - 19 Uhr · Sa. 8 - 19 Uhr · So. 9 - 16 Uhr</p>
      <p class="gap">Saisonausverkauf mit <span class="accent">-20% AUF MOTORRADBEKLEIDUNG</span></p>
      <p>und Zubehör - nur auf nicht reduzierte Lagerware</p>
      <p class="gap"><span class="accent">NETTOPREISE</span> auf Zubehör &amp; Bekleidung im Schnäppchenzelt</p>
      <p class="gap">Unsere <span class="accent">LIVEMUSIK</span> im Festzelt</p>
      <p>Freitag ab 20 Uhr Twistabend Nacht mit Kurvenfeger</p>
      <p>Samstag ab 20 Uhr Festmusik mit Bergklang-Alpin</p>
      <p>Sonntag 9 -16 Uhr Matinée</p>
    </section>

    <address class="contact">
      Talackerweg 14 · 5046 Hinterfeld<br>
      Tel. 062 418 30 72
    </address>

    <div class="partners">
      <span class="partner partner-vrx"><span class="dot"></span>VRX</span>
      <span class="partner partner-glp">GLP</span>
      <span class="partner partner-hanoka">Hanoka</span>
    </div>

    <div class="web-address">www.rad-kessel.ch</div>
  </main>
</body>
</html>
```